KORBALT

The business want a professional looking business card. We have a scetch we will add but want the extra upgrade, and would like more suggestions for variations of our business cards.

```html
<!DOCTYPE html>
<html lang="en">
<head>
<meta charset="utf-8">
<title>KORBALT business cards</title>
<link href="https://fonts.googleapis.com/css2?family=Arimo:wght@400;700&display=swap" rel="stylesheet">
<style>
  :root {
    --stage: #3d3d3d;
    --card: #ffffff;
    --gold: #a98545;
    --gold-light: #e8bd62;
    --bronze-dark: #6e4d24;
    --bronze-light: #ba9450;
    --ink-light: #ffffff;
    --ink-grey: #555555;
  }
  * { margin: 0; padding: 0; box-sizing: border-box; }
  html, body {
    width: 1200px; height: 1200px; overflow: hidden;
    background: var(--stage);
    font-family: "Arimo", Arial, sans-serif;
  }
  .stage { position: relative; width: 1200px; height: 1200px; }

  .card {
    position: absolute;
    background: var(--card);
    border-radius: 26px;
    overflow: hidden;
    box-shadow: 0 6px 18px rgba(0,0,0,0.35);
  }
  .card--front { left: 266px; top: 158px; width: 689px; height: 394px; }
  .card--back  { left: 262px; top: 653px; width: 689px; height: 394px; }

  .front-brand {
    position: absolute; left: 0; top: 0; width: 340px; height: 100%;
    display: flex; align-items: center; justify-content: center;
  }
  .wordmark {
    color: var(--gold);
    font-weight: 700;
    letter-spacing: 0.28em;
    font-size: 26px;
  }

  .accent-stripe {
    position: absolute; left: 340px; top: 0; width: 8px; height: 100%;
    background: var(--gold-light);
  }
  .contact-panel {
    position: absolute; left: 348px; top: 0; right: 0; height: 100%;
    background: linear-gradient(90deg, var(--bronze-dark) 0%, var(--bronze-light) 85%);
  }
  .divider-dot {
    position: absolute; left: 332px; top: 93px; width: 24px; height: 24px;
    border-radius: 50%; background: var(--gold-light);
    border: 3px solid var(--card);
  }
  .holder { position: absolute; left: 385px; top: 80px; color: var(--ink-light); }
  .holder__name { font-size: 21px; line-height: 1.2; }
  .holder__title { font-size: 15px; margin-top: 6px; }

  .contact-list {
    position: absolute; left: 385px; top: 201px; list-style: none;
    color: var(--ink-light); font-size: 15.5px;
  }
  .contact-list li { display: flex; align-items: center; height: 21px; }
  .contact-list svg { width: 12px; height: 12px; margin-right: 9px; flex: none; }

  .back-brand {
    position: absolute; left: 0; top: 150px; width: 100%;
    display: flex; justify-content: center;
  }
  .back-brand .wordmark { font-size: 40px; }
  .back-url {
    position: absolute; left: 0; top: 301px; width: 100%;
    text-align: center; color: var(--ink-grey);
    font-size: 16px; letter-spacing: 0.08em;
  }
</style>
</head>
<body>
<div class="stage">

  <section class="card card--front">
    <div class="front-brand"><span class="wordmark">KORBALT</span></div>
    <div class="contact-panel"></div>
    <div class="accent-stripe"></div>
    <div class="divider-dot"></div>

    <div class="holder">
      <p class="holder__name">Arne Solvik Haugen</p>
      <p class="holder__title">CEO &amp; Founder</p>
    </div>

    <ul class="contact-list">
      <li>
        <svg viewBox="0 0 12 12"><rect x="3" y="0.8" width="6" height="10.4" rx="1" fill="none" stroke="#fff" stroke-width="1.3"/><circle cx="6" cy="9.3" r="0.7" fill="#fff"/></svg>
        004791234567
      </li>
      <li>
        <svg viewBox="0 0 12 12"><rect x="0.5" y="2.5" width="11" height="7" fill="#fff"/><path d="M0.8 2.8 L6 6.6 L11.2 2.8" fill="none" stroke="#8a6a34" stroke-width="1"/></svg>
        contact@korbalt.llc
      </li>
      <li>
        <svg viewBox="0 0 12 12"><circle cx="6" cy="6" r="5.3" fill="#fff"/><path d="M4 2.5 Q6 4 4.5 6 Q7 7 6 9.8" fill="none" stroke="#8a6a34" stroke-width="1"/></svg>
        www.korbalt.llc
      </li>
    </ul>
  </section>

  <section class="card card--back">
    <div class="back-brand"><span class="wordmark">KORBALT</span></div>
    <p class="back-url">www.korbalt.llc</p>
  </section>

</div>
</body>
</html>
```